Insurance Law Website

**Please note do not sell insurance, we are a law firm which specialises in Insurance law.**

We are a legal insurance firm based in Australia consisting of 150+ legal professionals.

Our initial budget for this project is around: $500

We require a design to meet the specification below, however we do want designers to come up with an interpretation of something modern but still professional, we need it to stand out above all other legal websites!

1. Responsive design
2. It should be a minimalist design, the use of background imagery is fine but we are looking to de-clutter the home page in particular and have additional content accessible through menu links to other areas such as publications, news, announcements and expert/staff pages, careers etc.
3. Something that stands out from a typical legal website.
4. The homepage should cater for a video which will contain a 'who we are' message from the CEO/Firm.
5. Colours used light/medium blues (eg: #8aabff, #bdd7fc), white
6. We also require a static information box on the page with the heading "THREE STATES, ONE FOCUS" - see image attached for full text of the box.

Visitors to our website should be aware we are an Insurance law firm, this can be achieved by using insurance focused full background imagery (no natural disasters such as floods, earthquakes etc) such as insurance buildings (Harwick building - London), international landmarks etc

Some websites we like certain aspects of;

http://pellambraithwaite.com/ - top image boxes
http://www.vantel.com.au/ - similar however prefer to use a FULL background image, with one full width text box at the bottom, navigation menu at the top with logo

However please don't take these examples as a sign of what the site MUST look like, please use your imagination to interpret your own vision.

Reason: Extended due to feedback provided and waiting for resubmission of designs. It appears that some people may be misunderstanding the brief, please review the brief in full before submitting any designs and let us know if you have any questions.

Reason: Apologies to those who are waiting for a decision we are reviewing and discussiing all submitted designs internally and waiting for some additional amendments to come in. We have extended the project a final time whilst we carry out our reviews. Please continue to submit any modifications and thanks again for everyone's input thus far. D+T

We have 3 days left of this project please keep submitting your designs. This is a guaranteed project.

D+T

Target Market(s)

Lawyers looking for publications, information, contact details of our lawyers and careers/job searches.

Industry/Entity Type

Insurance

Font styles to use
Sans Serif

Requirements
Must have
• Top menu to include:

Home (small icon)
Who We Are (text)
Experts (text)
Expertise (text)
Media (text)
- News (text)
- Publications (text)
Community Footprint (text)
Careers (text)
Contact (text/icon)
Search (icon - will expand on click to search in field)

Footer to include:

Copyright (text)
Privacy Policy (text)
Cookie policy (text)
Sitemap (text)
Contact (text/icon)
Chainbook (icon)
Print (icon)
Email (icon)

Should not have
• Stereotypical imagery such as legal scales, money bags, natural disasters etc. We are a professional firm and require designs to suit.

```html
<!DOCTYPE html>
<html lang="en">
<head>
<meta charset="utf-8">
<title>Dalton Thorne — Insurance Law</title>
<link href="https://fonts.googleapis.com/css2?family=Open+Sans:wght@300;400;600&display=swap" rel="stylesheet">
<style>
  :root {
    --brand-blue: #1f4f9c;
    --nav-text: #1a1a1a;
    --white: #ffffff;
    --ink: #111111;
    --footer-bg: #050505;
    --hero-dark: #3c4048;
    --hero-mid: #8b929c;
    --hero-light: #c9d0da;
    --services-top: #6f9fdc;
    --services-bottom: #a9c6ea;
    --accent-line: #8aabff;
  }
  * { margin: 0; padding: 0; box-sizing: border-box; }
  html, body { width: 915px; height: 1200px; overflow: hidden; }
  body { font-family: "Open Sans", Arial, sans-serif; background: var(--white); color: var(--ink); position: relative; }

  .site-header { position: absolute; top: 0; left: 0; width: 915px; height: 50px; background: var(--white); }
  .brand { position: absolute; left: 10px; top: 1px; color: var(--brand-blue); font-size: 22px; line-height: 22px; font-weight: 400; }
  .brand span { display: block; }
  .brand-square { position: absolute; left: 118px; top: 4px; width: 26px; height: 26px; border: 1px solid var(--accent-line); }
  .main-nav { position: absolute; right: 52px; top: 20px; display: flex; gap: 10px; list-style: none; font-size: 10.5px; color: var(--nav-text); letter-spacing: -0.1px; }
  .main-nav .is-current { color: var(--brand-blue); }
  .search-icon { position: absolute; left: 866px; top: 12px; }

  .hero { position: absolute; top: 50px; left: 0; width: 915px; height: 430px; }
  .hero-image { position: absolute; inset: 0; background: linear-gradient(160deg, var(--hero-light) 0%, var(--hero-mid) 40%, var(--hero-dark) 100%); }
  .hero-title { position: absolute; top: 134px; left: 0; width: 915px; text-align: center; color: var(--white); font-weight: 300; font-size: 33px; line-height: 31px; letter-spacing: 7px; }
  .hero-actions { position: absolute; top: 226px; left: 301px; display: flex; align-items: center; gap: 26px; color: var(--white); font-size: 15px; }
  .btn-outline { border: 1.5px solid var(--white); padding: 2px 6px; line-height: 21px; }
  .watch-video { display: flex; align-items: center; gap: 8px; }

  .about { position: absolute; top: 480px; left: 0; width: 915px; height: 299px; background: var(--white); text-align: center; }
  .section-title { font-weight: 400; font-size: 45px; line-height: 50px; }
  .about .section-title { margin-top: 19px; }
  .title-rule { width: 283px; height: 3px; background: var(--ink); margin: 2px auto 0; }
  .about p { margin-top: 14px; font-size: 23.5px; line-height: 28.5px; }
  .btn-read-more { display: inline-block; margin-top: 46px; width: 171px; height: 43px; border: 2px solid var(--brand-blue); color: var(--brand-blue); font-size: 25px; line-height: 39px; }

  .services { position: absolute; top: 779px; left: 0; width: 915px; height: 270px; background: linear-gradient(180deg, var(--services-top), var(--services-bottom)); color: var(--white); text-align: center; }
  .services .section-title { margin-top: 11px; }
  .services .title-rule { background: var(--white); }
  .services p { margin-top: 12px; font-size: 23px; line-height: 28.8px; }

  .site-footer { position: absolute; top: 1049px; left: 0; width: 915px; height: 151px; background: var(--footer-bg); color: var(--white); }
  .footer-links { position: absolute; left: 11px; top: 118px; font-size: 15px; font-weight: 600; letter-spacing: -0.2px; }
  .footer-icons { position: absolute; left: 680px; top: 78px; display: flex; align-items: flex-end; gap: 8px; }
  .chainbook { width: 60px; height: 58px; border: 3px solid var(--white); display: flex; align-items: center; justify-content: center; font-size: 10.5px; font-weight: 600; }
</style>
</head>
<body>
  <header class="site-header">
    <div class="brand"><span>dalton</span><span>thorne</span></div>
    <div class="brand-square"></div>
    <ul class="main-nav">
      <li class="is-current">HOME</li>
      <li>WHO WE ARE</li>
      <li>EXPERTS</li>
      <li>EXPERTISE</li>
      <li>MEDIA</li>
      <li>COMMUNITY FOOTPRINT</li>
      <li>CAREERS</li>
      <li>CONTACT</li>
    </ul>
    <svg class="search-icon" width="28" height="28" viewBox="0 0 28 28" aria-label="Search">
      <circle cx="11" cy="11" r="8.5" fill="none" stroke="#222" stroke-width="3"/>
      <line x1="17" y1="17" x2="26" y2="26" stroke="#222" stroke-width="3.5" stroke-linecap="round"/>
    </svg>
  </header>

  <section class="hero">
    <div class="hero-image" role="img" aria-label="Upward view of the Harwick building in London with steel towers against a cloudy sky"></div>
    <h1 class="hero-title">THREE STATES.<br>ONE FOCUS.</h1>
    <div class="hero-actions">
      <span class="btn-outline">WHO WE ARE</span>
      <span class="watch-video">WATCH THE VIDEO
        <svg width="14" height="16" viewBox="0 0 14 16"><polygon points="0,0 14,8 0,16" fill="#1f4f9c"/></svg>
      </span>
    </div>
  </section>

  <section class="about">
    <h2 class="section-title">ABOUT US</h2>
    <div class="title-rule"></div>
    <p>We’re a legal insurance firm based in Australia consisting of over 150 legal<br>professionals. We offer a professional service with the expertise<br>required to meet your requirements.</p>
    <span class="btn-read-more">Read More</span>
  </section>

  <section class="services" role="img" aria-label="Blue-tinted photo of a classical building under a clear sky">
    <h2 class="section-title">SERVICES</h2>
    <div class="title-rule"></div>
    <p>Lorem ipsum dolor sit amet, consectetur adipiscing elit. In eros purus, dignissim<br>quis viverra nec, facilisis pretium nisi. Suspendisse pulvinar<br>et ipsum quis viverra. Duis vehicula nisi quis vulputate vehicula. Nulla venenatis<br>diam magna. Suspendisse accumsan gravida urna. Vivamus ornare hendrerit<br>ipsum, eu mollis purus consequat nec.</p>
  </section>

  <footer class="site-footer">
    <div class="footer-links">Copyright | Privacy Policy | Cookie Policy | Sitemap | Contact</div>
    <div class="footer-icons">
      <svg width="80" height="58" viewBox="0 0 80 58" aria-label="Email">
        <rect x="2" y="2" width="76" height="54" fill="none" stroke="#fff" stroke-width="3"/>
        <polyline points="2,2 40,34 78,2" fill="none" stroke="#fff" stroke-width="3"/>
        <line x1="2" y1="56" x2="31" y2="27" stroke="#fff" stroke-width="3"/>
        <line x1="78" y1="56" x2="49" y2="27" stroke="#fff" stroke-width="3"/>
      </svg>
      <svg width="62" height="58" viewBox="0 0 62 58" aria-label="Print">
        <rect x="14" y="1" width="34" height="16" fill="#fff"/>
        <rect x="1" y="16" width="60" height="28" rx="8" fill="#fff"/>
        <rect x="12" y="30" width="38" height="27" fill="#fff" stroke="#050505" stroke-width="3"/>
        <line x1="18" y1="40" x2="44" y2="40" stroke="#050505" stroke-width="3"/>
        <line x1="18" y1="48" x2="44" y2="48" stroke="#050505" stroke-width="3"/>
      </svg>
      <div class="chainbook">Chainbook</div>
    </div>
  </footer>
</body>
</html>
```